Heronby Mortgage Capital Business Card

We need a business card design for our mortgage servicing company. In addition to servicing the loans of homeowners, we help homeowners with purchasing their homes and any mortgage refinancing. We would like to see designs that use the colors in the logo attached below (gold-ish yellow and navy blue), and any other design you deem fit! The design should communicate a simpler life with smart mortgages provided by Heronby.

```html
<!DOCTYPE html>
<html lang="en">
<head>
<meta charset="utf-8">
<title>Heronby Mortgage Capital – Business Card</title>
<link href="https://fonts.googleapis.com/css2?family=Arimo:wght@400;700&display=swap" rel="stylesheet">
<style>
  :root {
    --navy: #262056;
    --gold: #d2a636;
    --paper: #f7f7f8;
    --ink: #1e1e2a;
    --backdrop: #2b2b2d;
  }
  * { margin: 0; padding: 0; box-sizing: border-box; }
  html, body { width: 1200px; height: 960px; overflow: hidden; }
  body {
    background: var(--backdrop);
    font-family: "Arimo", Arial, sans-serif;
    position: relative;
  }
  .card {
    position: absolute;
    left: 270px;
    width: 660px;
    height: 380px;
    border-radius: 26px;
    overflow: hidden;
  }
  .card-back { top: 70px; background: var(--navy); }
  .card-front { top: 510px; background: var(--paper); color: var(--ink); }

  .brand {
    display: flex;
    align-items: center;
    gap: 12px;
    color: var(--gold);
    font-weight: 700;
  }
  .brand-dot { border-radius: 50%; background: var(--gold); flex: none; }
  .card-back .brand {
    position: absolute; left: 0; right: 0; top: 160px;
    justify-content: center; font-size: 52px;
  }
  .card-back .brand-dot { width: 22px; height: 22px; }
  .card-front .brand {
    position: absolute; right: 48px; top: 62px; font-size: 28px;
  }
  .card-front .brand-dot { width: 12px; height: 12px; }

  .holder { position: absolute; left: 40px; top: 150px; }
  .holder-name { color: var(--gold); font-weight: 700; font-size: 28px; }
  .holder-title { color: var(--navy); font-size: 18px; margin-top: 2px; }

  .divider {
    position: absolute; left: 40px; right: 48px; top: 218px;
    height: 1.5px; background: var(--ink);
  }
  .address {
    position: absolute; left: 40px; top: 232px;
    font-size: 18px; line-height: 24px;
  }
  .contact {
    position: absolute; right: 48px; top: 232px;
    font-size: 18px; line-height: 26px; text-align: right;
  }
  .contact-line { display: flex; align-items: center; justify-content: flex-end; gap: 10px; }
  .contact-line svg { width: 16px; height: 16px; fill: var(--gold); }

  .band { position: absolute; left: 0; bottom: 0; width: 660px; height: 90px; }
  .website {
    position: absolute; right: 48px; bottom: 24px;
    color: #fff; font-size: 18px; letter-spacing: 5px;
  }
</style>
</head>
<body>
  <section class="card card-back">
    <div class="brand"><span class="brand-dot"></span>Heronby Mortgage</div>
  </section>

  <section class="card card-front">
    <div class="brand"><span class="brand-dot"></span>Heronby Mortgage</div>

    <div class="holder">
      <div class="holder-name">Daniel Harper</div>
      <div class="holder-title">President</div>
    </div>

    <div class="divider"></div>

    <address class="address" style="font-style:normal">
      4120 Alder Crest Lane<br>
      Maple Hollow, NY 11990
    </address>

    <div class="contact">
      <div class="contact-line">(555) 8120-4471
        <svg viewBox="0 0 24 24" aria-hidden="true"><path d="M6.6 10.8a15.1 15.1 0 0 0 6.6 6.6l2.2-2.2c.3-.3.7-.4 1-.2 1.1.4 2.3.6 3.6.6.6 0 1 .4 1 1V20c0 .6-.4 1-1 1A17 17 0 0 1 3 4c0-.6.4-1 1-1h3.5c.6 0 1 .4 1 1 0 1.3.2 2.5.6 3.6.1.3 0 .7-.2 1z"/></svg>
      </div>
      <div class="contact-line">name@heronby.com
        <svg viewBox="0 0 24 24" aria-hidden="true"><path d="M2 5h20v14H2z M2 5l10 8 10-8" stroke="#f7f7f8" stroke-width="1.5"/></svg>
      </div>
    </div>

    <svg class="band" viewBox="0 0 660 90" aria-hidden="true">
      <polygon points="0,26 300,26 318,44 0,44" fill="var(--gold)"/>
      <polygon points="0,46 320,46 340,26 660,26 660,90 0,90" fill="var(--navy)"/>
    </svg>
    <div class="website">www.heronby.com</div>
  </section>
</body>
</html>
```